Current website re-design to a updated look and feel.

We currently have a website www.brightlanefreight.com that we want to give an updated look and feel to. We are a logistics company that competes with Harbex, Dm Whitfield, Tarn but on a smaller scale. We want something fresh and updated. We have two locations one in downtown Chicago, IL and one in Palatine IL. We are a fun group that also gets the job done. We know we need pictures of both locations and possibly a video, but we need fresh design ideas. The 'who we are' page is really the only page that we currently want to keep. The 'what we do' page needs to be completely re-done from a look and feel for sure.

Target Market(s)

Anyone who uses Truck transportation to move their product. Mainly US manufacturers.

Industry/Entity Type

Logistics

Number of Pages Required

5+ page

Font styles to use
Sans Serif

Colors
5c91c4
0355a3
d0dfed

Requirements
Must have
• The new design must entice people to want to do business with us. The design must have locations for pictures and at least one video which we know we will have to provide. Design must be easy to navigate.

```html
<!DOCTYPE html>
<html lang="en">
<head>
<meta charset="utf-8">
<title>Brightlane Freight</title>
<link href="https://fonts.googleapis.com/css2?family=Titillium+Web:wght@300;400;600;700&family=Open+Sans:wght@400;600&display=swap" rel="stylesheet">
<style>
:root{
  --blue:#0355a3;
  --sky:#5c91c4;
  --pale:#d0dfed;
  --accent:#3fb6e8;
  --red:#e2231a;
  --ink:#1a1a1a;
  --grey:#6b6b6b;
  --bg-grey:#eeeff0;
}
*{margin:0;padding:0;box-sizing:border-box}
html,body{width:1120px;height:1200px;overflow:hidden;background:#fff}
body{position:relative;font-family:"Open Sans",sans-serif;color:var(--ink)}
.abs{position:absolute}
.brand{left:106px;top:24px;display:flex;align-items:center;gap:8px;font-family:"Titillium Web",sans-serif;font-weight:400;font-size:36px;line-height:40px;color:var(--blue);letter-spacing:-0.5px}
.brand .dot{width:12px;height:12px;border-radius:50%;background:var(--sky)}
.info{top:21px;font-family:"Titillium Web",sans-serif}
.info .label{font-size:9.5px;color:#999;display:flex;align-items:center;gap:5px}
.info .value{font-size:11.5px;color:#333;margin-top:5px}
.sep{top:18px;width:1px;height:36px;background:#ddd}
.navband{left:0;top:98px;width:1120px;height:22px;background:var(--blue)}
.nav{left:324px;top:74px;width:796px;height:46px;background:var(--blue);clip-path:polygon(24px 0,100% 0,100% 100%,0 100%,0 24px)}
.nav-item{top:74px;height:46px;line-height:46px;font-family:"Titillium Web",sans-serif;font-weight:600;font-size:11.5px;color:#fff}
.nav-active{left:366px;top:116px;width:41px;height:3px;background:var(--red)}
.nav-div{left:945px;top:92px;width:1px;height:10px;background:#fff}
.social{top:92px;width:9px;height:9px;border-radius:2px;background:#fff}
.hero{left:0;top:120px;width:1120px;height:440px;
  background:
    radial-gradient(ellipse 60% 40% at 70% 75%,rgba(150,62,44,.75),transparent 70%),
    radial-gradient(ellipse 40% 35% at 20% 85%,rgba(40,110,120,.7),transparent 70%),
    linear-gradient(180deg,#34465e 0%,#55647a 22%,#8c97a3 40%,#6a5a52 55%,#4c3e3a 75%,#2e4552 100%)}
.hero-box{left:122px;top:201px;width:431px;height:304px;background:rgba(3,85,163,0.5)}
.bar{width:40px;height:3px;background:var(--accent)}
.hero-title{left:160px;top:270px;font-family:"Titillium Web",sans-serif;font-weight:600;font-size:39px;line-height:48px;color:#fff}
.hero-text{left:158px;top:386px;width:212px;font-family:"Titillium Web",sans-serif;font-weight:600;font-size:12.4px;line-height:23px;color:#fff}
.welcome-title{left:120px;top:640px;font-family:"Titillium Web",sans-serif;font-weight:300;font-size:29px;color:var(--blue)}
.welcome-text{left:120px;top:694px;width:430px;font-size:11.2px;line-height:20.8px;color:var(--grey)}
.founder{left:120px;top:900px;font-family:"Titillium Web",sans-serif;font-weight:600;font-size:13.5px}
.video{left:576px;top:618px;width:432px;height:287px;
  background:
    radial-gradient(ellipse 45% 50% at 25% 45%,rgba(170,70,60,.55),transparent 70%),
    radial-gradient(ellipse 40% 45% at 75% 30%,rgba(120,70,50,.6),transparent 70%),
    radial-gradient(ellipse 50% 40% at 55% 85%,rgba(230,225,215,.7),transparent 70%),
    linear-gradient(120deg,#6d6a66,#b9a99a 45%,#8a9cad 80%,#5b7fa6)}
.play{left:759px;top:730px;width:64px;height:64px;border-radius:50%;background:var(--sky);border:3px solid #fff;display:flex;align-items:center;justify-content:center}
.services{left:0;top:966px;width:1120px;height:234px;background:var(--bg-grey)}
.services-title{left:120px;top:1058px;font-family:"Titillium Web",sans-serif;font-weight:400;font-size:29px;line-height:34px;color:var(--blue)}
.services-text{left:121px;top:1152px;width:196px;font-size:11.2px;line-height:21px;color:var(--grey)}
.card{top:1030px;width:204px;height:170px;background:#fff}
.card .photo{height:136px}
.card .name{padding:23px 0 0 24px;font-family:"Titillium Web",sans-serif;font-weight:700;font-size:11px;color:var(--blue);letter-spacing:0.3px}
</style>
</head>
<body>
<header>
  <div class="abs brand"><span>Brightlane</span><span class="dot"></span></div>
  <div class="abs info" style="left:583px"><div class="label"><svg width="10" height="10" viewBox="0 0 10 10"><path d="M1 6V5a4 4 0 0 1 8 0v1M1 6h2v3H1zM7 6h2v3H7z" fill="none" stroke="#333" stroke-width="1.2"/></svg>Call Us Anytime</div><div class="value">847.555.0142</div></div>
  <div class="abs sep" style="left:697px"></div>
  <div class="abs info" style="left:721px"><div class="label"><svg width="10" height="10" viewBox="0 0 10 10"><circle cx="5" cy="5" r="4" fill="none" stroke="#333" stroke-width="1.2"/><path d="M5 2.5V5h2" fill="none" stroke="#333" stroke-width="1.2"/></svg>Opening Time</div><div class="value">08:00 - 18:00</div></div>
  <div class="abs sep" style="left:825px"></div>
  <div class="abs info" style="left:848px"><div class="label"><svg width="11" height="9" viewBox="0 0 11 9"><rect x="0.5" y="0.5" width="10" height="8" fill="none" stroke="#333"/><path d="M0.5 0.5l5 4 5-4" fill="none" stroke="#333"/></svg>Email Us</div><div class="value">Rates@brightlanefreight.com</div></div>
</header>
<nav>
  <div class="abs navband"></div>
  <div class="abs nav"></div>
  <a class="abs nav-item" style="left:368px">Home</a>
  <a class="abs nav-item" style="left:434px">What We Do</a>
  <a class="abs nav-item" style="left:530px">How We Do It</a>
  <a class="abs nav-item" style="left:633px">Who We Are</a>
  <a class="abs nav-item" style="left:729px">Tracking</a>
  <a class="abs nav-item" style="left:806px">Chat</a>
  <a class="abs nav-item" style="left:865px">Contact</a>
  <div class="abs nav-active"></div>
  <div class="abs nav-div"></div>
  <span class="abs social" style="left:962px"></span>
  <span class="abs social" style="left:978px"></span>
  <span class="abs social" style="left:995px"></span>
  <span class="abs social" style="left:1016px"></span>
</nav>
<section>
  <div class="abs hero" role="img" aria-label="Container port with stacked shipping containers and cranes under a cloudy sky"></div>
  <div class="abs hero-box"></div>
  <div class="abs bar" style="left:158px;top:254px"></div>
  <h1 class="abs hero-title">SEA &amp; OCEAN<br>DELIVERY</h1>
  <p class="abs hero-text">Lorem Ipsum is simply dummy text of the printing and typesetting industry. Lorem Ipsum has been the.</p>
</section>
<section>
  <div class="abs bar" style="left:120px;top:618px"></div>
  <h2 class="abs welcome-title">WELCOME FROM OUR FOUNDER</h2>
  <p class="abs welcome-text">Brightlane Freight welcomes you to our growing family of clients! We have over 26 years of experience in helping people solve their logistics needs from coast-to-coast. We also provide friendly, exceptional service that makes it easy to do business with us. Give us a call today and experience the difference for yourself!<br>"Our service commitment begins from the moment you contact us. We appreciate your trust, and we go the extra mile to ensure that your freight is handled with care and expediency. If an issue comes up, we work tirelessly to resolve it, staying in contact with you until your freight is delivered without issue!”</p>
  <div class="abs founder">Marian Holt, Founder</div>
  <div class="abs video" role="img" aria-label="Video still of a team meeting around an office table"></div>
  <div class="abs play"><svg width="22" height="22" viewBox="0 0 22 22"><path d="M6 3l14 8-14 8z" fill="#fff"/></svg></div>
</section>
<section>
  <div class="abs services"></div>
  <div class="abs bar" style="left:120px;top:1031px"></div>
  <h2 class="abs services-title">SPECLAL<br>SERVICES</h2>
  <p class="abs services-text">There are many variations of passages of Lorem Ipsum available, but the</p>
  <div class="abs card" style="left:348px"><div class="photo" role="img" aria-label="Container terminal at dusk" style="background:radial-gradient(ellipse 70% 35% at 50% 80%,rgba(150,70,50,.6),transparent 70%),linear-gradient(180deg,#1f3a5e,#3d5877 40%,#7d8590 55%,#4f4a46 75%,#2f4b4c)"></div><div class="name">FREIGHT MANAGEMENT</div></div>
  <div class="abs card" style="left:576px"><div class="photo" role="img" aria-label="Highway with light trails at sunset" style="background:radial-gradient(ellipse 50% 20% at 50% 30%,rgba(240,150,90,.8),transparent 70%),linear-gradient(180deg,#4f6379,#b07a5c 30%,#4b5563 55%,#2b3138)"></div><div class="name">TRANSPORTATION</div></div>
  <div class="abs card" style="left:804px"><div class="photo" role="img" aria-label="Red semi truck on the road" style="background:radial-gradient(ellipse 45% 30% at 50% 70%,rgba(200,30,35,.85),transparent 70%),linear-gradient(180deg,#3f7fc0,#a7c6e3 50%,#8a7a62 78%,#4d4c48)"></div><div class="name">CARRIERS</div></div>
</section>
</body>
</html>
```